Propose a revamped landing page

One template we like eg is https://www.trovask.com but but cluttered Our logo and colors are attached to our logo and colors are printed on a white background what we have. So font usage ...
1 page

```html
<!DOCTYPE html>
<html lang="en">
<head>
<meta charset="utf-8">
<title>Switch Scout – Always switch to the cheapest energy provider</title>
<link href="https://fonts.googleapis.com/css2?family=Raleway:wght@400;500;600;700&display=swap" rel="stylesheet">
<style>
  :root {
    --orange: #f5a31a;
    --slate: #3f4a52;
    --ink: #111111;
    --band: #fcefd4;
    --white: #ffffff;
    --badge: #d8d8d8;
  }
  * { box-sizing: border-box; margin: 0; padding: 0; }
  html, body { width: 1200px; height: 2500px; overflow: hidden; background: var(--white); }
  body { font-family: "Raleway", Arial, sans-serif; color: var(--ink); position: relative; }

  .site-header .brand { position: absolute; left: 233px; top: 58px; display: flex; align-items: center; gap: 8px;
    font-size: 24px; font-weight: 700; color: var(--orange); }
  .brand-dot { width: 14px; height: 14px; border-radius: 50%; background: var(--orange); }
  .social { position: absolute; left: 863px; top: 62px; display: flex; gap: 6px; list-style: none; }
  .social li { width: 13px; height: 13px; background: var(--ink); border-radius: 2px; }

  .main-nav { position: absolute; left: 0; top: 120px; width: 1200px; height: 30px; background: var(--band); }
  .main-nav ul { list-style: none; display: flex; gap: 27px; padding-left: 240px; line-height: 30px;
    font-size: 14px; font-weight: 500; }

  .hero { position: absolute; left: 0; top: 240px; width: 1200px; text-align: center; }
  .hero-brand { display: inline-flex; align-items: center; gap: 16px; font-size: 84px; font-weight: 700;
    color: var(--orange); line-height: 1; }
  .hero-brand .mark { width: 52px; height: 52px; border-radius: 50%; background: var(--orange); }
  .hero-tagline { margin-top: 38px; font-size: 22px; line-height: 28px; color: var(--ink); }
  .cta { display: inline-block; margin-top: 30px; width: 250px; height: 46px; line-height: 46px; border-radius: 23px;
    background: var(--orange); color: var(--ink); font-size: 20px; text-decoration: none; }
  .press { margin-top: 64px; font-size: 13px; font-weight: 700; }
  .press-badges { display: flex; justify-content: center; gap: 14px; margin-top: 12px; }
  .press-badges span { width: 70px; height: 12px; background: var(--badge); border-radius: 2px; }
  .press-badges span:last-child { width: 36px; }

  .section { position: absolute; left: 233px; width: 760px; }
  .section h2 { color: var(--orange); font-weight: 600; font-size: 37px; line-height: 45px; }
  .section p { font-size: 18px; line-height: 22.5px; }
  .intro { top: 738px; }
  .intro h2 { margin-bottom: 32px; }
  .intro p { width: 510px; margin-bottom: 22px; }

  .pricing { top: 1164px; }
  .pricing h2 { margin-bottom: 18px; }
  .price-list { list-style: none; margin-top: 16px; font-size: 18px; line-height: 22.5px; }
  .price-list li::before { content: ""; display: inline-block; width: 12px; height: 12px; border-radius: 50%;
    background: var(--ink); margin-right: 10px; }
  .footnote { margin-top: 28px; font-size: 9.5px !important; line-height: 12px !important; width: 705px; }

  .steps { top: 1560px; }
  .steps h2 { font-size: 44px; line-height: 56px; margin-bottom: 14px; }
  .steps h3 { font-size: 21px; font-weight: 500; line-height: 24px; }
  .steps p { width: 410px; margin-bottom: 24px; }

  .benefits-title { position: absolute; top: 1990px; left: 0; width: 1200px; text-align: center; color: var(--orange);
    font-size: 44px; font-weight: 600; }
  .benefit { position: absolute; top: 2105px; width: 230px; }
  .benefit svg { display: block; margin: 0 0 40px 58px; }
  .benefit h3 { font-size: 21px; font-weight: 600; line-height: 24px; }
  .benefit p { font-size: 18px; line-height: 22.5px; }
  .b1 { left: 233px; } .b2 { left: 512px; } .b3 { left: 778px; }

  .site-footer { position: absolute; top: 2470px; left: 0; width: 1200px; text-align: center; font-size: 17px; font-weight: 700; }
</style>
</head>
<body>
  <header class="site-header">
    <div class="brand"><span>Switch Scout</span><span class="brand-dot"></span></div>
    <ul class="social" aria-label="Social links"><li></li><li></li><li></li><li></li><li></li></ul>
  </header>

  <nav class="main-nav">
    <ul>
      <li>THAT'S HOW IT WORKS</li><li>PRICES</li><li>ASK?</li><li>ABOUT US</li>
      <li>OPERATIONS</li><li>EXPERIENCE</li><li>PRESS</li>
    </ul>
  </nav>

  <section class="hero">
    <div class="hero-brand"><span>Switch Scout</span><span class="mark"></span></div>
    <p class="hero-tagline">Always automatically switch to the<br>cheapest energy provider</p>
    <a class="cta" href="#">REGISTER NOW</a>
    <p class="press">Known from</p>
    <div class="press-badges"><span></span><span></span><span></span></div>
  </section>

  <section class="section intro">
    <h2>Never pay too much for electricity<br>&amp; gas again</h2>
    <p>Gone are the days of bad deals, tedious rate comparison and boring exchange forms.</p>
    <p>With the automatic change service for Switch Scouts you will never again pay too much<br>for electricity and gas. And that, without touching a finger. We fight for you through the<br>tariff jungle.</p>
    <p>So save your hard earned money and become a Switch Scout.</p>
  </section>

  <section class="section pricing">
    <h2>The cheapest of all super powers</h2>
    <p>From 24 euros you are there:</p>
    <ul class="price-list">
      <li>Service for electricity or gas (1 meter): 24 euros / year</li>
      <li>Service for electricity and gas (2 counters): 36 Euro / year</li>
      <li>The first fee will be charged only after your first change</li>
      <li>Save up to 850 euros annually electricity and gas costs<br>at the first change *</li>
    </ul>
    <p class="footnote">* Annual saving of an average Austrian household (3,500 kWh of electricity and 15,000 kWh of gas consumption) in the region with the greatest savings potential after the first change from the most widely used tariff of the local electricity and gas provider to the cheapest available provider according to the PriceWatch price monitor of 2.11. 2018.</p>
  </section>

  <section class="section steps">
    <h2>How do I become a Switch Scout?</h2>
    <h3>1. Once login</h3>
    <p>upload financial statements. Select preferences. Finish the registration.</p>
    <h3>2. Automatic</h3>
    <p>fare change We pick the cheapest fare for you and carry out the change automatically.</p>
    <h3>3. Sit back and save money</h3>
    <p>Always switch automatically to the low fare.</p>
  </section>

  <h2 class="benefits-title">Register once, always save</h2>

  <div class="benefit b1">
    <svg width="84" height="84" viewBox="0 0 84 84" aria-hidden="true">
      <circle cx="42" cy="42" r="42" fill="var(--orange)"/>
      <path d="M22 42 L62 24 L52 62 L42 48 Z" fill="var(--white)"/>
      <path d="M42 48 L62 24" stroke="var(--orange)" stroke-width="3"/>
    </svg>
    <h3>independently</h3>
    <p>We work only for you. In order to remain independent, we consciously do without commission deals with energy providers.</p>
  </div>

  <div class="benefit b2">
    <svg width="100" height="84" viewBox="0 0 100 84" aria-hidden="true">
      <g fill="var(--orange)">
        <circle cx="36" cy="50" r="22"/>
        <rect x="32" y="22" width="8" height="56" rx="2"/>
        <rect x="8" y="46" width="56" height="8" rx="2"/>
        <rect x="32" y="22" width="8" height="56" rx="2" transform="rotate(45 36 50)"/>
        <rect x="32" y="22" width="8" height="56" rx="2" transform="rotate(-45 36 50)"/>
        <circle cx="72" cy="22" r="12"/>
        <rect x="69" y="6" width="6" height="32" rx="2"/>
        <rect x="56" y="19" width="32" height="6" rx="2"/>
        <circle cx="84" cy="48" r="7"/>
      </g>
      <circle cx="36" cy="50" r="8" fill="var(--white)"/>
      <circle cx="72" cy="22" r="5" fill="var(--white)"/>
      <circle cx="84" cy="48" r="3" fill="var(--white)"/>
    </svg>
    <h3>automatically</h3>
    <p>You sign up once and we'll do the rest. All automatically.</p>
  </div>

  <div class="benefit b3">
    <svg width="84" height="84" viewBox="0 0 84 84" aria-hidden="true">
      <rect x="6" y="12" width="74" height="56" rx="6" fill="var(--orange)"/>
      <rect x="46" y="28" width="38" height="22" rx="11" fill="var(--white)"/>
      <rect x="50" y="32" width="30" height="14" rx="7" fill="var(--orange)"/>
      <circle cx="58" cy="39" r="4" fill="var(--white)"/>
    </svg>
    <h3>fair</h3>
    <p>Switch Scouts stays more in Börsel. Despite service charge.</p>
  </div>

  <footer class="site-footer">CONDITION / DATA PROTECTION / IMPRINT</footer>
</body>
</html>
```